依頼詳細
基本レイアウトについては
https://zuvaro.com/diagrams/7kq2m94T3XhpleWn
もしくは、添付データのワイヤーをご参照ください。

全体の雰囲気としては
http://www.morelid.co.jp/eco/forest/
のような和風・職人の雰囲気がありつつも、
あまり古臭くならないようなイメージを希望いたします。

色合いについては特に制限はないですが、上記を踏まえ
赤(エンジ)・オレンジ・紫・緑・ベージュなどが良いかと思います。

提出の写真素材があまり多くないのですが、
http://boxquiltry.jp/download/8fa27cd04b91e5a36d0c2bb7105e94f2d6a1c479
にアップロードしたものをご利用いただければ幸いです。

また、
http://vomre.jp/
などから、5000円程度までならこちらにて購入可能です。
カンプデータにて作成頂き、納品時に当方にて購入したデータに差し替えていただければと存じます。

【ロゴについて】
ロゴについては代表の家紋である
「剣片喰 (けんかたばみ)」を使用します。
添付データにjpgのデータを添付しております。
色合いについては、必ずしも黒である必要はないので、デザインに合わせて
ご調整いただいて結構です。

ページ数
1ページ
希望イメージ
シンプル 複雑
単色 カラフル
暗い 明るい
日常 高級
遊び心 厳粛
未来的 伝統的
女性的 男性的
希望する色
特に規定はないですが、和風をイメージを取り入れた色合いを希望します。
納品ファイル
• 高解像度JPG (.jpg)
• フォトショップ形式 (.psd)
補足説明
先方提出のイメージ写真については
下記URLからダウンロードしてご利用ください。

また、
http://vomre.jp/

【参考サイト】
hhttp://www.morelid.co.jp/eco/forest/
→全体の構成、誠実な印象とコンテンツの見やすさを気に入られています。
→色合いについては、必ずしもグリーンベースである必要はありません。

基本的には和風・職人の雰囲気を出すようなサイトが希望なのですが、
あまり和風すぎる、職人すぎる印象は出したくない要望がございます。
(代表自体が35歳と若いこと、マンションの緑地管理などを出していく希望があるため)

http://tokuvane.jp/
のような雰囲気だと、少し古臭すぎる印象がございます。

とはいえ
http://www.qrv-jp.com/
のような感じですと少しポップすぎる印象です

http://plinth-galore.com/2012/166.html
http://plinth-galore.com/2011/115.html
→フッター部分の参照
■ 選んだ理由

クライアントとの協議の結果、こちらの案を採用させて頂きました。
職人っぽい雰囲気でありつつ、今っぽい印象を残したデザインが
選考の決め手になりました。

■ 提案者全員のお礼・コメント

この度は多数ご提案いただきありがとうございました。
当選に至らなかったランサー様には大変心苦しいのですが、
次の機会がございましたら、是非ご提案頂ければ幸いです。
引続きよろしくお願いいたします。

```html
<!DOCTYPE html>
<html lang="ja">
<head>
<meta charset="utf-8">
<title>緑匠園 | 植木屋・造園・外構・緑地管理</title>
<link rel="stylesheet" href="https://fonts.googleapis.com/css2?family=Noto+Sans+JP:wght@400;700&family=Noto+Serif+JP:wght@500;700&display=swap">
<style>
:root{
  --crimson:#8a1838;
  --crimson-dark:#6e1029;
  --green:#4f7f1f;
  --green-dark:#3b6414;
  --beige:#efe8da;
  --paper:#f7f3ea;
  --page:#e4e1da;
  --ink:#3a2e28;
  --muted:#7a6d63;
  --line:#d8cdbb;
  --white:#fff;
}
*{box-sizing:border-box;margin:0;padding:0}
html,body{width:741px;height:1200px;overflow:hidden}
body{background:var(--page);font-family:"Noto Sans JP",sans-serif;color:var(--ink);font-size:8px;position:relative}
.serif{font-family:"Noto Serif JP",serif}
.wrap{position:absolute;left:69px;width:603px}

.site-header{position:absolute;top:0;left:0;width:741px;height:37px;background:var(--white)}
.brand{position:absolute;left:94px;top:8px;display:flex;align-items:center;gap:6px}
.brand-mark{width:18px;height:18px;border-radius:50%;background:var(--crimson)}
.brand-name{font-family:"Noto Serif JP",serif;font-weight:700;font-size:18px;color:var(--crimson);letter-spacing:3px}
.header-contact{position:absolute;left:455px;top:5px;text-align:left}
.header-contact .label{font-size:7px;color:var(--muted)}
.header-contact .tel{font-size:15px;font-weight:700;color:var(--crimson);letter-spacing:.5px;line-height:1.2}
.header-contact .hours{font-size:6px;color:var(--muted)}
.header-address{position:absolute;left:575px;top:7px;font-size:7px;color:var(--muted)}

.global-nav{position:absolute;top:37px;left:0;width:741px;height:22px;background:var(--crimson)}
.global-nav ul{list-style:none;display:flex;position:absolute;left:69px;width:603px;height:22px}
.global-nav li{flex:1;color:var(--white);font-size:8px;text-align:center;line-height:22px;border-right:1px solid rgba(255,255,255,.25)}
.global-nav li:last-child{border-right:0}

.hero{position:absolute;top:59px;left:69px;width:603px;height:205px}
.hero-photo{position:absolute;inset:0;background:linear-gradient(160deg,#5d7b3c 0%,#38522a 45%,#6c6a50 75%,#8f8a6e 100%)}
.hero-caption{position:absolute;left:0;right:0;bottom:0;height:28px;background:rgba(40,30,20,.45);color:var(--white);font-size:13px;text-align:center;line-height:28px;letter-spacing:1px}

.sidebar{position:absolute;left:69px;top:267px;width:171px}
.side-banner{height:34px;background:linear-gradient(90deg,#6f8b4b,#a9b98c);position:relative}
.side-banner span{position:absolute;right:6px;top:10px;font-size:8px;font-weight:700;color:var(--white);background:var(--crimson);padding:2px 4px}
.contact-box{margin-top:0;height:139px;background:var(--green);position:relative;color:var(--white)}
.contact-photo{position:absolute;left:6px;top:6px;width:50px;height:46px;background:linear-gradient(135deg,#9aa47a,#5e6b45)}
.contact-title{position:absolute;left:60px;top:12px;font-size:11px;font-weight:700;line-height:1.4}
.contact-title em{font-style:normal;color:#ffe08a}
.contact-sub{position:absolute;left:6px;top:62px;font-size:8px}
.contact-tel{position:absolute;left:6px;top:76px;width:159px;height:28px;background:var(--white);color:var(--crimson);font-size:18px;font-weight:700;text-align:center;line-height:28px}
.contact-mail{position:absolute;left:6px;top:110px;width:159px;height:22px;background:var(--crimson);font-size:8px;text-align:center;line-height:22px}
.side-menu{list-style:none;margin-top:6px;background:var(--white);border:1px solid var(--line)}
.side-menu li{height:28px;line-height:28px;padding-left:16px;font-size:8px;border-bottom:1px solid var(--line);position:relative}
.side-menu li:last-child{border-bottom:0}
.side-menu li::before{content:"";position:absolute;left:6px;top:11px;border:3px solid transparent;border-left:4px solid var(--crimson)}

.main{position:absolute;left:247px;top:267px;width:425px}
.section-title{height:22px;background:var(--crimson);color:var(--white);font-size:11px;line-height:22px;padding-left:24px;position:relative}
.section-title::before{content:"";position:absolute;left:7px;top:6px;width:10px;height:10px;background:#c9a84a;border-radius:50%}
.section-title.green{background:var(--white);color:var(--green-dark);border-bottom:2px solid var(--green)}
.section-title.green::before{background:var(--green)}
.news{list-style:none;background:var(--white);padding:4px 8px}
.news li{display:flex;height:21px;line-height:21px;border-bottom:1px dotted var(--line);font-size:7px}
.news time{width:70px;color:var(--crimson)}
.intro{margin-top:10px;height:203px;background:var(--paper);border:1px solid var(--line);position:relative}
.intro-heading{position:absolute;left:10px;top:10px;width:250px;font-size:11px;line-height:1.7}
.tag{display:inline-block;color:var(--white);font-size:9px;padding:0 4px;margin-right:2px}
.tag.a{background:var(--crimson)}.tag.b{background:var(--green)}.tag.c{background:#c06a1d}.tag.d{background:#6c3a7a}
.intro-heading strong{font-size:14px;color:var(--crimson)}
.intro-text{position:absolute;left:10px;top:100px;width:260px;font-size:7px;line-height:1.7;color:var(--muted)}
.intro-photo{position:absolute;right:8px;top:8px;width:140px;height:120px;background:linear-gradient(150deg,#b6a789,#7d7358 60%,#5f6b44)}
.works{margin-top:10px}
.works-grid{display:grid;grid-template-columns:repeat(3,1fr);gap:8px;padding:8px;background:var(--white)}
.work-photo{height:100px;background:linear-gradient(160deg,#a39377,#6d7a4f)}
.work-cap{font-size:7px;margin-top:3px;height:20px;color:var(--muted)}
.more{display:block;margin:8px 0 0 auto;width:150px;height:22px;background:var(--green);color:var(--white);font-size:8px;line-height:22px;text-align:center}

.site-footer{position:absolute;top:1037px;left:0;width:741px;height:163px;background:var(--crimson)}
.footer-brand{position:absolute;left:94px;top:14px;display:flex;align-items:center;gap:6px}
.footer-brand .brand-mark{background:var(--white)}
.footer-brand .brand-name{color:var(--white);font-size:16px}
.footer-info{position:absolute;left:94px;top:42px;color:var(--white);font-size:7px;line-height:1.7}
.footer-links{position:absolute;left:250px;top:16px;display:flex;gap:24px}
.footer-links ul{list-style:none}
.footer-links li{color:var(--white);font-size:7px;line-height:17px;padding-left:8px;position:relative}
.footer-links li::before{content:"";position:absolute;left:0;top:6px;border:2px solid transparent;border-left:3px solid var(--white)}
.footer-tel{position:absolute;left:487px;top:14px;width:185px;height:40px;background:var(--white);text-align:center}
.footer-tel .label{font-size:7px;color:var(--muted);margin-top:3px}
.footer-tel .tel{font-size:17px;font-weight:700;color:var(--crimson);line-height:1.3}
.footer-mail{position:absolute;left:487px;top:62px;width:185px;height:24px;background:#c06a1d;color:var(--white);font-size:8px;text-align:center;line-height:24px}
.copyright{position:absolute;left:0;bottom:0;width:741px;height:20px;background:var(--crimson-dark);color:var(--white);font-size:6px;text-align:center;line-height:20px}
</style>
</head>
<body>

<header class="site-header">
  <div class="brand"><span class="brand-mark"></span><span class="brand-name">緑匠園</span></div>
  <div class="header-contact">
    <p class="label">お電話でのお問い合わせ</p>
    <p class="tel">0120-418-962</p>
    <p class="hours">受付 8:00〜18:00</p>
  </div>
  <p class="header-address">神奈川県川崎市幸区緑ヶ丘2-4-7</p>
</header>

<nav class="global-nav">
  <ul>
    <li>ホーム</li><li>植木屋の仕事</li><li>造園・外構工事</li><li>マンション緑地管理</li><li>施工事例</li><li>よくあるご質問</li><li>会社案内</li>
  </ul>
</nav>

<section class="hero">
  <div class="hero-photo" role="img" aria-label="手入れされた和風庭園と植木の写真"></div>
  <p class="hero-caption serif">お庭のことなら、どんなことでもお気軽にご相談ください</p>
</section>

<aside class="sidebar">
  <div class="side-banner" role="img" aria-label="マンションの植栽の写真"><span>マンション緑地管理のご提案</span></div>
  <div class="contact-box">
    <div class="contact-photo" role="img" aria-label="作業中の職人の写真"></div>
    <p class="contact-title serif"><em>見積無料</em>・<br>お問い合わせ</p>
    <p class="contact-sub">お気軽にお問い合わせください</p>
    <p class="contact-tel">0120-418-962</p>
    <p class="contact-mail">メールでのお問い合わせ</p>
  </div>
  <ul class="side-menu">
    <li>トップページ</li><li>植木屋の仕事について</li><li>造園・外構工事について</li><li>マンション緑地管理</li><li>施工事例</li><li>よくあるご質問</li><li>会社案内</li><li>お問い合わせ</li>
  </ul>
</aside>

<main class="main">
  <section>
    <h2 class="section-title serif">新着情報</h2>
    <ul class="news">
      <li><time>2013年1月1日</time>新着情報のタイトルが入ります。お知らせの内容です。</li>
      <li><time>2013年1月1日</time>新着情報のタイトルが入ります。お知らせの内容です。</li>
      <li><time>2013年1月1日</time>新着情報のタイトルが入ります。お知らせの内容です。</li>
      <li><time>2013年1月1日</time>新着情報のタイトルが入ります。お知らせの内容です。</li>
      <li><time>2013年1月1日</time>新着情報のタイトルが入ります。お知らせの内容です。</li>
      <li><time>2013年1月1日</time>新着情報のタイトルが入ります。お知らせの内容です。</li>
    </ul>
  </section>

  <section class="intro">
    <h2 class="intro-heading serif">神奈川県川崎市幸区の<br>
      <span class="tag a">植木屋</span><span class="tag b">造園</span><span class="tag c">外構</span><span class="tag d">緑地管理</span>は<br>
      <strong>緑匠園</strong>にお任せ下さい。</h2>
    <p class="intro-text">庭木の剪定から造園・外構工事、マンションの緑地管理まで、経験豊富な職人が丁寧に対応いたします。小さなお庭のお手入れもお気軽にご相談ください。地域の皆様に愛される庭づくりを心がけております。</p>
    <div class="intro-photo" role="img" aria-label="剪定作業を行う職人の写真"></div>
  </section>

  <section class="works">
    <h2 class="section-title green serif">施工事例</h2>
    <div class="works-grid">
      <div><div class="work-photo" role="img" aria-label="施工事例の庭の写真"></div><p class="work-cap">○○様　造園工事</p></div>
      <div><div class="work-photo" role="img" aria-label="施工事例の庭の写真"></div><p class="work-cap">○○様　外構工事</p></div>
      <div><div class="work-photo" role="img" aria-label="施工事例の庭の写真"></div><p class="work-cap">○○マンション　緑地管理</p></div>
      <div><div class="work-photo" role="img" aria-label="施工事例の庭の写真"></div><p class="work-cap">○○様　造園工事</p></div>
      <div><div class="work-photo" role="img" aria-label="施工事例の庭の写真"></div><p class="work-cap">○○様　剪定</p></div>
      <div><div class="work-photo" role="img" aria-label="施工事例の庭の写真"></div><p class="work-cap">○○様　外構工事</p></div>
    </div>
    <span class="more">施工事例をもっと見る ▶</span>
  </section>
</main>

<footer class="site-footer">
  <div class="footer-brand"><span class="brand-mark"></span><span class="brand-name">緑匠園</span></div>
  <p class="footer-info">〒212-0000<br>神奈川県川崎市幸区緑ヶ丘2-4-7<br>TEL 0120-418-962</p>
  <div class="footer-links">
    <ul><li>トップページ</li><li>植木屋の仕事について</li><li>造園・外構工事について</li><li>マンション緑地管理</li></ul>
    <ul><li>施工事例</li><li>よくあるご質問</li><li>会社案内</li><li>お問い合わせ</li></ul>
  </div>
  <div class="footer-tel">
    <p class="label">お電話でのお問い合わせ</p>
    <p class="tel">0120-418-962</p>
  </div>
  <p class="footer-mail">メールでのお問い合わせ</p>
  <p class="copyright">Copyright © 緑匠園 All Rights Reserved.</p>
</footer>

</body>
</html>
```